Stylist/Barber Standup Sign for Hair Regrowth Company

We want to design an attractive and eye-catching sign for hair stylists and barbers to sit on their workstations to attract the attention of their clients regarding hair loss and encourage them to speak to their stylist about it of they are would like to seek treatment.
50% of men and 25% of women suffer from hair loss but most are in denial that it is happening or too embarrassed to talk about it.

Copy for the flyer is as follows:

[Section 1:]
This flyer has been placed here/designed to spark conversation about hair loss

[Section 2:]
The truth is...
73% of people believe their hair is thinning
They are right

[Section 3:]
If you've got questions, your stylist or barber has answers.

Additional Background Information:

Primary target audience is men between the ages of 25-45, secondary target audience is men 46-60

Current Consumer Perception? (in the first person) “I’ve been thinking about my hair. I think it’s getting thinner and I’m scared, worried and don’t know what to do. But I don’t know if there is anything that really works. I’ve tried other things and nothing‘s worked.”

Tonality of materials? Very guy friendly, matter of fact, authoritative, its what you might hear from your best friend. Confident. Encouraging, but with a sense of urgency.

Please use our brand colors, but do not include our logo or brand name.
Colors are as follows:
Green: #4ca26f
Light Grey: #999999
Dark Grey: #262626

I have attached print templates in both PDF and Jpeg, please use those to provide final ready to print documents if you are selected.

Target Market(s)

Industry/Entity Type

Health And Wellness

Font styles to use
Sans Serif

Colors
00a990
ffffff
333333
cbcbcb

Requirements
Must have
• We want to get across the following messaging. Ideally you will submit a design using our copy and if you think you can do better, please feel free to submit another design with your own copy/messaging. If you can do it better we would love to select you :-)
• Our copy?
• This flyer has been placed here/designed to spark conversation about hair loss
• The truth is...
• 73% of people believe their hair is thinning
• They are right
• If you've got questions, your stylist or barber has answers
• Also please use our brand colors:
• Green: #4ca26f
• Light Grey: #999999
• Dark Grey: #262626
Should not have
• dont add any logos, images or ornate design. this needs to be simple, easy to ready and eye catching.
• do not use the color red in any capacity.

```html
<!DOCTYPE html>
<html lang="en">
<head>
<meta charset="utf-8">
<title>Hair Loss Conversation Stand-up Sign</title>
<link href="https://fonts.googleapis.com/css2?family=Montserrat:wght@500;600&family=Lato:wght@400;700;900&display=swap" rel="stylesheet">
<style>
  :root {
    --green: #4ca26f;
    --dark: #232323;
    --panel-grey: #d8d8d8;
    --rule-grey: #8a8a8a;
    --paper: #ffffff;
    --backdrop: #e4e4e9;
    --ink: #1e1e1e;
  }
  * { box-sizing: border-box; margin: 0; padding: 0; }
  html, body {
    width: 1200px;
    height: 954px;
    overflow: hidden;
    background: var(--backdrop);
  }
  .sign {
    position: absolute;
    left: 290px;
    top: 17px;
    width: 620px;
    height: 920px;
    background: var(--paper);
    padding: 20px;
  }
  .sign-inner {
    width: 580px;
    height: 880px;
    background: var(--panel-grey);
    display: flex;
    flex-direction: column;
  }
  .stats {
    display: block;
    width: 580px;
    height: 300px;
  }
  .stat-number {
    font-family: "Montserrat", sans-serif;
    font-weight: 600;
    font-size: 118px;
    fill: #ffffff;
    letter-spacing: -2px;
  }
  .stat-label {
    font-family: "Montserrat", sans-serif;
    font-weight: 600;
    font-size: 38px;
    fill: #ffffff;
  }
  .band {
    text-align: center;
    color: #ffffff;
    font-family: "Lato", sans-serif;
  }
  .band-denial {
    background: var(--dark);
    margin-top: 10px;
    padding: 17px 40px;
    font-size: 19px;
    line-height: 1.3;
  }
  .band-truth {
    background: var(--green);
    margin-top: 10px;
    padding: 24px 20px 22px;
  }
  .truth-title {
    font-weight: 900;
    font-size: 46px;
    line-height: 1.1;
  }
  .truth-stat {
    font-size: 21px;
    margin-top: 6px;
  }
  .band-answers {
    background: var(--dark);
    padding: 20px 20px;
    font-size: 22px;
    line-height: 1.3;
  }
  .brief-notes {
    flex: 1;
    padding: 18px 30px 0;
    text-align: center;
    font-family: "Lato", sans-serif;
    color: var(--ink);
  }
  .note-heading {
    font-weight: 900;
    font-size: 32px;
    color: var(--green);
    line-height: 1.15;
  }
  .note-body {
    font-size: 19px;
    line-height: 1.3;
    margin-top: 4px;
  }
  .note-rule {
    border: 0;
    border-top: 2px solid var(--rule-grey);
    margin: 12px 10px 10px;
  }
</style>
</head>
<body>
  <main class="sign">
    <div class="sign-inner">
      <svg class="stats" viewBox="0 0 580 300" aria-label="50% of men, 25% of women">
        <rect x="0" y="0" width="290" height="240" fill="var(--dark)"/>
        <rect x="290" y="0" width="290" height="240" fill="var(--green)"/>
        <polygon points="0,300 42,232 290,232 290,300" fill="var(--green)"/>
        <polygon points="290,232 546,232 580,300 290,300" fill="var(--dark)"/>
        <text class="stat-number" x="148" y="168" text-anchor="middle">50%</text>
        <text class="stat-number" x="432" y="208" text-anchor="middle">25%</text>
        <text class="stat-label" x="165" y="280" text-anchor="middle">of Men</text>
        <text class="stat-label" x="430" y="282" text-anchor="middle">of Women</text>
      </svg>

      <section class="band band-denial">
        Suffer From Hair Loss But Most Are In Denial That It Is Happening Or Too Embarrassed To Talk About It.
      </section>

      <section class="band band-truth">
        <h1 class="truth-title">The Truth is...</h1>
        <p class="truth-stat">73% of people believe their hair is thinning They are right</p>
      </section>

      <section class="band band-answers">
        If you've got questions,<br>your stylist or barber has answers
      </section>

      <section class="brief-notes">
        <h2 class="note-heading">Tonality Of Materials?</h2>
        <p class="note-body">Very guy friendly, matter of fact, authoritative, its what you might hear from your best friend. Confident. Encouraging, but with a sense of urgency.</p>
        <hr class="note-rule">
        <h2 class="note-heading">Current Consumer Perception?</h2>
        <p class="note-body">I've been thinking about my hair. I think it's getting thinner and I'm scared, worried and don't know what to do. But I don't know if there is anything that really works. I've tried other things and nothing's worked.</p>
      </section>
    </div>
  </main>
</body>
</html>
```